BRAVEN VOLTWORKS SERVICES needs a vibrant design for electrical contracting work.

I require a card design for my own electrical contracting business. I will be doing a lot of domestic and commercial work, including things such as repairs, maintenance, lighting, installations and various others. LED lighting and energy efficiency will be a big part of my business. I wish not to have childish pictures such as light bulbs in the design, but rather a smart and modern looking card which incorporates my logo colours and perhaps the same lighting strike within the faded background of the card.

Target Market(s)

Residential and Commercial property owners.

Industry/Entity Type

Electrical

Contact Information for Business Card

Dario Pesek
EC40362
Phone Number: 0417 538 924
Email: dario@bravenvoltworks.com

Font styles to use
Serif
Sans Serif

Requirements
Must have
• My Logo and associated colours.
Nice to have
• Some form of shapes splitting the card into different colours related to the colours of my logo. Electric Blue, Silver/Grey and White.
Should not have
• Childish pictures and symbols such as light bulbs.

```html
<!DOCTYPE html>
<html lang="en">
<head>
<meta charset="utf-8">
<title>Braven Voltworks Services – Business Card</title>
<link href="https://fonts.googleapis.com/css2?family=Exo+2:wght@400;500;600&display=swap" rel="stylesheet">
<style>
  :root{
    --page-bg:#e8e8ea;
    --card-white:#ffffff;
    --electric-blue:#3a5fc0;
    --silver-light:#dfe0e2;
    --silver-dark:#b6b8bc;
    --text-grey:#6d6f73;
    --text-white:#ffffff;
  }
  html,body{margin:0;padding:0;width:1200px;height:1023px;overflow:hidden;background:var(--page-bg);}
  .business-card{
    position:absolute;left:170px;top:262px;width:860px;height:500px;
    border-radius:34px;overflow:hidden;background:var(--card-white);
    box-shadow:0 10px 30px rgba(0,0,0,.18);
    font-family:"Exo 2",sans-serif;
  }
  .card-shapes{position:absolute;inset:0;}
  .brand{position:absolute;left:56px;top:74px;display:flex;align-items:center;gap:18px;}
  .brand-dot{width:54px;height:54px;border-radius:50%;background:var(--electric-blue);flex:none;}
  .brand-name{font-size:34px;font-weight:600;color:var(--electric-blue);letter-spacing:1px;white-space:nowrap;}
  .holder{position:absolute;left:128px;top:190px;}
  .holder-name{font-size:27px;font-weight:500;color:var(--electric-blue);white-space:nowrap;}
  .holder-role{font-size:17px;color:var(--text-grey);}
  .divider{margin:0 12px;color:var(--text-grey);font-weight:400;}
  .licence{font-size:17px;color:var(--text-grey);margin-top:6px;letter-spacing:1px;}
  .contacts{position:absolute;left:56px;top:396px;list-style:none;margin:0;padding:0;}
  .contacts li{display:flex;align-items:center;gap:14px;color:var(--text-white);font-size:20px;margin-bottom:14px;letter-spacing:.5px;white-space:nowrap;}
  .contact-icon{width:22px;height:22px;flex:none;}
</style>
</head>
<body>
  <div class="business-card">
    <svg class="card-shapes" width="860" height="500" viewBox="0 0 860 500" aria-hidden="true">
      <defs>
        <linearGradient id="blueBand" x1="0" y1="0" x2="1" y2="1">
          <stop offset="0" stop-color="#2f4fa8"/>
          <stop offset="1" stop-color="#4f78d6"/>
        </linearGradient>
        <linearGradient id="silverLine" x1="0" y1="0" x2="1" y2="0">
          <stop offset="0" stop-color="#d8d9dc"/>
          <stop offset=".5" stop-color="#9ea0a5"/>
          <stop offset="1" stop-color="#e2e3e5"/>
        </linearGradient>
      </defs>
      <rect class="card-base" width="860" height="500" fill="#ffffff"/>
      <polygon class="grey-block-light" points="660,500 860,250 860,500" fill="#dfe0e2"/>
      <polygon class="grey-block-dark" points="740,500 860,350 860,500" fill="#b6b8bc"/>
      <polygon class="silver-edge" points="0,358 702,358 636,500 624,500 688,366 0,366" fill="url(#silverLine)"/>
      <polygon class="blue-band" points="0,372 680,372 620,500 0,500" fill="url(#blueBand)"/>
    </svg>

    <div class="brand">
      <span class="brand-dot"></span>
      <span class="brand-name">BRAVEN VOLTWORKS SERVICES</span>
    </div>

    <div class="holder">
      <div class="holder-name">Dario Pesek<span class="divider">|</span><span class="holder-role">Director</span></div>
      <div class="licence">EC40362</div>
    </div>

    <ul class="contacts">
      <li>
        <svg class="contact-icon" viewBox="0 0 22 22" aria-hidden="true">
          <rect width="22" height="22" rx="4" fill="#ffffff"/>
          <path d="M7 5c1 0 1.6 2.2 1.6 2.8 0 .7-1 1-1 1.6.4 1.6 2.3 3.6 4 4 .6 0 .9-1 1.6-1 .6 0 2.8.6 2.8 1.6 0 1-1.2 2-2.4 2C9 16 6 13 5 8.4 5 6.2 6 5 7 5z" fill="#3a5fc0"/>
        </svg>
        <span class="contact-phone">0417 538 924</span>
      </li>
      <li>
        <svg class="contact-icon" viewBox="0 0 22 22" aria-hidden="true">
          <rect width="22" height="22" rx="4" fill="#ffffff"/>
          <rect x="4.5" y="6.5" width="13" height="9" fill="none" stroke="#3a5fc0" stroke-width="1.6"/>
          <path d="M4.5 6.5l6.5 5 6.5-5" fill="none" stroke="#3a5fc0" stroke-width="1.6"/>
        </svg>
        <span class="contact-email">dario@bravenvoltworks.com</span>
      </li>
    </ul>
  </div>
</body>
</html>
```